Copperfox Billboard

Please design a billboard using my photos and logos.
For photo of truck please crop the truck itself out and not have the trees / dirt in photo.
Please put " Best Prices in Sevier County"
Please put " 30-yard Dumpsters Starting at 600.00"
Please put " 16-yard Dumpsters Starting at 300.0"
Please put " Delivery and Pickup 7 Days a week"
Billboard size will be 10 ft tall 30 ft wide

```html
<!DOCTYPE html>
<html lang="en">
<head>
<meta charset="utf-8">
<title>Copperfox Billboard</title>
<link rel="stylesheet" href="https://fonts.googleapis.com/css2?family=Anton&family=Oswald:wght@400;500;700&family=Poppins:wght@600&display=swap">
<style>
  :root {
    --backdrop: #8b8b8b;
    --ink: #0a0a0a;
    --purple: #7b3f9e;
    --white: #ffffff;
  }
  html, body {
    margin: 0;
    padding: 0;
    width: 1051px;
    height: 1200px;
    overflow: hidden;
    background: var(--backdrop);
  }
  .billboard {
    position: absolute;
    left: 35px;
    top: 436px;
    width: 980px;
    height: 327px;
    background: var(--ink);
    overflow: hidden;
    box-shadow: 0 4px 12px rgba(0,0,0,0.35);
  }
  .torn-band {
    position: absolute;
    inset: 0;
  }
  .brand {
    position: absolute;
    left: 30px;
    top: 38px;
    display: flex;
    align-items: center;
    gap: 10px;
    z-index: 2;
  }
  .brand-dot {
    width: 26px;
    height: 26px;
    border-radius: 50%;
    background: var(--purple);
  }
  .brand-name {
    font-family: "Anton", sans-serif;
    font-size: 44px;
    line-height: 1;
    color: var(--white);
    letter-spacing: 1px;
  }
  .headline {
    position: absolute;
    left: 283px;
    top: 28px;
    margin: 0;
    font-family: "Anton", sans-serif;
    font-weight: 400;
    font-size: 50px;
    line-height: 1;
    color: var(--white);
    letter-spacing: 3.4px;
    white-space: nowrap;
    z-index: 2;
  }
  .service {
    position: absolute;
    left: 378px;
    top: 104px;
    margin: 0;
    font-family: "Oswald", sans-serif;
    font-style: italic;
    font-weight: 700;
    line-height: 1;
    white-space: nowrap;
    z-index: 3;
  }
  .service-days {
    display: block;
    font-size: 40px;
    color: var(--purple);
    text-transform: uppercase;
  }
  .service-week {
    display: block;
    margin-top: 4px;
    font-size: 40px;
    font-weight: 500;
    color: var(--white);
    text-transform: uppercase;
  }
  .price-badge {
    position: absolute;
    top: 116px;
    width: 132px;
    height: 122px;
    background: var(--purple);
    clip-path: polygon(100% 50%, 93.2% 58.6%, 96.2% 69.2%, 86.6% 74.5%, 85.4% 85.4%, 74.5% 86.6%, 69.2% 96.2%, 58.6% 93.2%, 50% 100%, 41.4% 93.2%, 30.8% 96.2%, 25.5% 86.6%, 14.6% 85.4%, 13.4% 74.5%, 3.8% 69.2%, 6.8% 58.6%, 0% 50%, 6.8% 41.4%, 3.8% 30.8%, 13.4% 25.5%, 14.6% 14.6%, 25.5% 13.4%, 30.8% 3.8%, 41.4% 6.8%, 50% 0%, 58.6% 6.8%, 69.2% 3.8%, 74.5% 13.4%, 85.4% 14.6%, 86.6% 25.5%, 96.2% 30.8%, 93.2% 41.4%);
    display: flex;
    flex-direction: column;
    align-items: center;
    justify-content: center;
    font-family: "Oswald", sans-serif;
    color: var(--white);
    text-align: center;
    line-height: 1.05;
    z-index: 2;
  }
  .price-badge--large { left: 52px; }
  .price-badge--small { left: 211px; }
  .badge-size { font-size: 15px; font-weight: 400; text-transform: uppercase; }
  .badge-label { font-size: 7px; font-weight: 500; margin-top: 3px; text-transform: uppercase; }
  .badge-price { font-size: 27px; font-weight: 400; margin-top: 1px; }
  .website {
    position: absolute;
    left: 29px;
    top: 266px;
    font-family: "Poppins", sans-serif;
    font-weight: 600;
    font-size: 34.5px;
    line-height: 1;
    color: var(--white);
    white-space: nowrap;
    z-index: 2;
  }
  .truck-photo {
    position: absolute;
    left: 617px;
    top: 97px;
    width: 363px;
    height: 230px;
    clip-path: polygon(30% 0, 100% 0, 100% 100%, 8% 100%, 0 75%, 0 23%, 30% 23%);
    background: linear-gradient(100deg, #e9e9ec 0%, #d4d4d8 45%, #5a2d78 70%, #3e1f55 100%);
    z-index: 1;
  }
</style>
</head>
<body>
  <main class="billboard">
    <svg class="torn-band" viewBox="0 0 980 327" width="980" height="327" aria-hidden="true">
      <path fill="var(--white)" d="M0 242 L40 233 L90 240 L140 228 L200 236 L250 224 L300 230 L340 218 L380 210 L420 204 L445 198 L480 208 L520 216 L560 224 L600 232 L630 254 L660 267 L980 250 L980 327 L0 327 Z"/>
      <path fill="var(--purple)" d="M0 250 L40 242 L90 249 L140 237 L200 245 L250 233 L300 239 L340 227 L380 219 L420 213 L445 207 L480 217 L520 225 L560 233 L600 241 L630 262 L660 275 L980 258 L980 327 L0 327 Z"/>
    </svg>

    <div class="brand">
      <span class="brand-dot"></span>
      <span class="brand-name">COPPERFOX</span>
    </div>

    <h1 class="headline">BEST PRICES IN SEVIER COUNTY</h1>

    <div class="price-badge price-badge--large">
      <span class="badge-size">30-Yard<br>Dumpsters</span>
      <span class="badge-label">Starting at</span>
      <span class="badge-price">600.00</span>
    </div>
    <div class="price-badge price-badge--small">
      <span class="badge-size">16-Yard<br>Dumpsters</span>
      <span class="badge-label">Starting at</span>
      <span class="badge-price">300.0</span>
    </div>

    <div class="truck-photo" role="img" aria-label="White roll-off truck carrying a purple dumpster"></div>

    <p class="service">
      <span class="service-days">Delivery &amp; Pickup</span>
      <span class="service-week">7 Days a Week</span>
    </p>

    <div class="website">www.copperfoxdumpsters.com</div>
  </main>
</body>
</html>
```